Qivera Health & Wellness Business Card Design

We would like to create business cards matching with our new logo design. The card should be professional looking but still have a playful side and something that would be eye catching. We are planing to open a luxury medical spa and looking to create a design based on this new logo. We are looking for a design that shows off luxury but not be gold in color. Also, while we are a more female oriented medical center we do have men that come in for our services and it should be be too feminine.

Target Market(s)

Health & Wellness. Medical patients. Luxury spa

Industry/Entity Type

Health And Wellness

Contact Information for Business Card

It should have the logo design in the front of card and back of card should have our contact information. Our current colors are peach/ coral, teal, and gray. We are looking for a modern looking design.

Font styles to use
Script

Colors
32a6d6
e667a6
86cfc6
fece3e

Requirements
Must have
• It should have our logo design. We would prefer to have a more modern look to the card.
Nice to have
• Eye-Catching Design on the personable side but still classy.
Should not have
• At this point we are looking for the best design. It should not have color purple.

```html
<!DOCTYPE html>
<html lang="en">
<head>
<meta charset="utf-8">
<title>Qivera Health &amp; Wellness – Business Cards</title>
<link rel="stylesheet" href="https://fonts.googleapis.com/css2?family=Roboto+Condensed:wght@700&family=Arimo:wght@400&display=swap">
<style>
  :root {
    --backdrop: #9a9da1;
    --card-dark: #25262a;
    --coral: #f29891;
    --white: #ffffff;
    --ghost: #151618;
  }
  * { margin: 0; padding: 0; box-sizing: border-box; }
  html, body { width: 1189px; height: 1200px; overflow: hidden; background: var(--backdrop); }
  .sheet { position: relative; width: 1189px; height: 1200px; }
  .card {
    position: absolute; width: 432px; height: 259px; border-radius: 12px; overflow: hidden;
    background: var(--card-dark); box-shadow: 0 3px 6px rgba(0,0,0,.35);
  }
  .card--back { background: var(--coral); display: flex; align-items: center; justify-content: center; }
  .card__band { position: absolute; left: 0; right: 0; bottom: 0; height: 12px; background: var(--coral); }
  .card__ghost {
    position: absolute; right: -30px; top: 60px; font-family: "Roboto Condensed", sans-serif;
    font-weight: 700; font-size: 92px; color: var(--ghost); letter-spacing: 1px; white-space: nowrap;
  }
  .brand {
    position: absolute; left: 27px; top: 70px; display: flex; align-items: center; gap: 8px;
    font-family: "Arimo", sans-serif; font-size: 19px; color: var(--coral); white-space: nowrap;
  }
  .brand__dot { width: 12px; height: 12px; border-radius: 50%; background: var(--coral); }
  .card--back .brand { position: static; font-size: 26px; color: #111; }
  .card--back .brand__dot { background: #111; width: 16px; height: 16px; }
  .person {
    position: absolute; left: 23px; top: 153px; font-family: "Roboto Condensed", sans-serif;
    font-weight: 700; font-size: 19px; color: var(--white); white-space: nowrap;
  }
  .person__role {
    font-family: "Arimo", sans-serif; font-weight: 400; font-size: 11px; margin-left: 4px;
    padding-left: 5px; border-left: 1px solid var(--white);
  }
  .contact {
    position: absolute; left: 24px; top: 181px; list-style: none;
    font-family: "Arimo", sans-serif; font-size: 11.5px; color: var(--white); line-height: 14.8px;
  }
  .contact li { display: flex; align-items: center; gap: 4px; white-space: nowrap; }
  .contact svg { width: 9px; height: 9px; fill: var(--coral); flex: none; }
  .contact .gap { margin-left: 10px; }
  .accent { color: var(--coral); }
</style>
</head>
<body>
<svg width="0" height="0" style="position:absolute">
  <defs>
    <symbol id="i-phone" viewBox="0 0 10 10"><path d="M2 0h2l1 3-1.5 1a6 6 0 0 0 2.5 2.5L7 5l3 1v2c0 1-1 2-2 2A8 8 0 0 1 0 2c0-1 1-2 2-2z"/></symbol>
    <symbol id="i-fax" viewBox="0 0 10 10"><rect x="2.5" y="0" width="5" height="3"/><rect x="0" y="3.5" width="10" height="4.5" rx="1"/><rect x="2.5" y="7" width="5" height="3"/></symbol>
    <symbol id="i-mail" viewBox="0 0 10 10"><path d="M0 2h10v6H0z M0 2l5 3.5L10 2" /></symbol>
    <symbol id="i-globe" viewBox="0 0 10 10"><circle cx="5" cy="5" r="5"/></symbol>
    <symbol id="i-pin" viewBox="0 0 10 10"><path d="M5 0a3.6 3.6 0 0 1 3.6 3.6C8.6 6 5 10 5 10S1.4 6 1.4 3.6A3.6 3.6 0 0 1 5 0zm0 2a1.5 1.5 0 1 0 0 3 1.5 1.5 0 0 0 0-3z"/></symbol>
  </defs>
</svg>

<main class="sheet">
  <!-- Row 1 -->
  <article class="card" style="left:145px;top:61px">
    <div class="card__ghost" aria-hidden="true">Qivera</div>
    <div class="brand"><span class="brand__dot"></span>Qivera Health &amp; Wellness</div>
    <h2 class="person">TAMSIN ROWE, MD</h2>
    <ul class="contact">
      <li><svg><use href="#i-phone"/></svg>(555) 410-2236<svg class="gap"><use href="#i-fax"/></svg>(555) 410-2290</li>
      <li><svg><use href="#i-mail"/></svg>info@qiverawellness.com</li>
      <li><svg><use href="#i-globe"/></svg>www.<span class="accent">qiverawellness</span>.com</li>
      <li><svg><use href="#i-pin"/></svg>14 Alder Lane, Suite 4, Northfield NJ 07012</li>
    </ul>
    <div class="card__band"></div>
  </article>

  <article class="card" style="left:620px;top:61px">
    <div class="card__ghost" aria-hidden="true">Qivera</div>
    <div class="brand"><span class="brand__dot"></span>Qivera Health &amp; Wellness</div>
    <h2 class="person">KELSEY LORNE<span class="person__role">Office Manager</span></h2>
    <ul class="contact">
      <li><svg><use href="#i-phone"/></svg>(555) 410-2236<svg class="gap"><use href="#i-fax"/></svg>(555) 410-2290</li>
      <li><svg><use href="#i-mail"/></svg>info@qiverawellness.com</li>
      <li><svg><use href="#i-globe"/></svg>www.<span class="accent">qiverawellness</span>.com</li>
      <li><svg><use href="#i-pin"/></svg>14 Alder Lane, Suite 4, Northfield NJ 07012</li>
    </ul>
    <div class="card__band"></div>
  </article>

  <!-- Row 2 -->
  <article class="card" style="left:145px;top:339px">
    <div class="card__ghost" aria-hidden="true">Qivera</div>
    <div class="brand"><span class="brand__dot"></span>Qivera Health &amp; Wellness</div>
    <h2 class="person">CARLA WHITFIELD, PT</h2>
    <ul class="contact">
      <li><svg><use href="#i-phone"/></svg>(555) 410-2236<svg class="gap"><use href="#i-fax"/></svg>(555) 410-2290</li>
      <li><svg><use href="#i-mail"/></svg>info@qiverawellness.com</li>
      <li><svg><use href="#i-globe"/></svg>www.<span class="accent">qiverawellness</span>.com</li>
      <li><svg><use href="#i-pin"/></svg>14 Alder Lane, Suite 4, Northfield NJ 07012</li>
    </ul>
    <div class="card__band"></div>
  </article>

  <article class="card" style="left:620px;top:339px">
    <div class="card__ghost" aria-hidden="true">Qivera</div>
    <div class="brand"><span class="brand__dot"></span>Qivera Health &amp; Wellness</div>
    <h2 class="person">JULIET SEVERIN<span class="person__role">Marketing Director</span></h2>
    <ul class="contact">
      <li><svg><use href="#i-phone"/></svg>(555) 410-2236<svg class="gap"><use href="#i-fax"/></svg>(555) 410-2290</li>
      <li><svg><use href="#i-mail"/></svg>marketing@qiverawellness.com</li>
      <li><svg><use href="#i-globe"/></svg>www.<span class="accent">qiverawellness</span>.com</li>
      <li><svg><use href="#i-pin"/></svg>14 Alder Lane, Suite 4, Northfield NJ 07012</li>
    </ul>
    <div class="card__band"></div>
  </article>

  <!-- Row 3 -->
  <article class="card" style="left:145px;top:618px">
    <div class="card__ghost" aria-hidden="true">Qivera</div>
    <div class="brand"><span class="brand__dot"></span>Qivera Health &amp; Wellness</div>
    <h2 class="person">DANA MORROW, NP</h2>
    <ul class="contact">
      <li><svg><use href="#i-phone"/></svg>(555) 410-2236<svg class="gap"><use href="#i-fax"/></svg>(555) 410-2290</li>
      <li><svg><use href="#i-mail"/></svg>info@qiverawellness.com</li>
      <li><svg><use href="#i-globe"/></svg>www.<span class="accent">qiverawellness</span>.com</li>
      <li><svg><use href="#i-pin"/></svg>14 Alder Lane, Suite 4, Northfield NJ 07012</li>
    </ul>
    <div class="card__band"></div>
  </article>

  <article class="card card--back" style="left:620px;top:618px">
    <div class="brand"><span class="brand__dot"></span>Qivera Health &amp; Wellness</div>
  </article>

  <!-- Row 4 -->
  <article class="card" style="left:143px;top:897px;width:436px">
    <div class="card__ghost" aria-hidden="true">Qivera</div>
    <div class="brand"><span class="brand__dot"></span>Qivera Health &amp; Wellness</div>
    <h2 class="person">JENNA HOLLIS<span class="person__role">Managing Director</span></h2>
    <ul class="contact">
      <li><svg><use href="#i-phone"/></svg>(555) 410-2236<svg class="gap"><use href="#i-fax"/></svg>(555) 410-2290</li>
      <li><svg><use href="#i-mail"/></svg>info@qiverawellness.com</li>
      <li><svg><use href="#i-globe"/></svg>www.<span class="accent">qiverawellness</span>.com</li>
      <li><svg><use href="#i-pin"/></svg>14 Alder Lane, Suite 4, Northfield NJ 07012</li>
    </ul>
    <div class="card__band"></div>
  </article>
</main>
</body>
</html>
```